Brochure condensed from the PDF marketing

An organised brochure with 4 x banner heading for the various portfolios,
Condensed and made into a 4 page booklet or neat and tidy brochure display that can be easily emailed to prospective customers. The brochure should be neat and professional similar content to the website to send the 4 x Portfolios to the various Industry Categories, thank you

** Ive just uploaded a couple of extra photos for the ' Our Services ' area on the Brochure, pls add the ice cream one for the ' Parfait Cleaning and Sanitisation Services, and on the ' Our Services' category for the High pressure Gurney and Playground Cleaning pls add a fun photo for example the one I sent with people having fun on the playground equipment, **
Updates

HI KW Designer The brochure design is for my facebook title page /Users/user/Desktop/Screenshot 2020-05-05 at 9.22.39 PM.png Under Brightwell Facebook Design (Contest) DO you have a direct email, its very difficult to keep posing images and updates here Thank you Loretta @ Brightwell.

Target Market(s)

Cleaning Services

Font styles to use
Serif

Requirements
Must have
• Look professional and neat and tidy brochure booklet for marketing on email to prospective customers.

```html
<!DOCTYPE html>
<html lang="en">
<head>
<meta charset="utf-8">
<title>Brightwell – Our Services Brochure</title>
<link href="https://fonts.googleapis.com/css2?family=Open+Sans:wght@400;600;700&display=swap" rel="stylesheet">
<style>
:root{
  --navy:#143f73;
  --orange:#e8501c;
  --ink:#333a40;
  --paper:#ffffff;
  --bg:#ffffff;
  --rule:#1b1b1b;
  --table-head:#c9d8ea;
  --table-pink:#f0d5d8;
}
*{box-sizing:border-box;margin:0;padding:0}
html,body{width:1200px;height:1200px;overflow:hidden;background:var(--bg)}
body{font-family:"Open Sans",Arial,sans-serif;color:var(--ink);position:relative}
.page{position:absolute;top:218px;width:514px;height:726px;background:var(--paper);box-shadow:0 2px 10px rgba(0,0,0,.22)}
.page--services{left:65px}
.page--more{left:645px}
.col{position:absolute;display:flex;flex-direction:column}
.section-title{color:var(--navy);font-weight:700;font-size:8.6px;line-height:1.2}
.brand-title{font-size:11px;font-weight:700;color:var(--ink);line-height:1.15}
.brand-title .accent{color:var(--orange)}
.subtitle{font-size:8.6px;font-weight:700;color:var(--ink);line-height:1.3}
.shot{position:relative;margin:8px 0 0 6px}
.shot .frame{background:#fff;padding:4px;box-shadow:0 1px 5px rgba(0,0,0,.3);position:relative;z-index:1}
.shot .fill{display:block;width:100%;height:100%}
.shot::before{content:"";position:absolute;right:-9px;top:-6px;width:27px;height:26px;border-top:2px solid var(--orange);border-right:2px solid var(--orange)}
.shot::after{content:"";position:absolute;left:-6px;bottom:-7px;width:24px;height:22px;border-bottom:2px solid var(--orange);border-left:2px solid var(--orange)}
.intro{font-size:5.4px;line-height:1.3;margin-top:17px}
.label{font-size:6.3px;font-weight:700;color:#222;margin-top:6px}
.checklist{list-style:none;display:grid;grid-template-columns:1fr 1fr;column-gap:10px;row-gap:4px;margin-top:5px;font-size:5.4px;line-height:1.25}
.checklist.single{grid-template-columns:1fr}
.checklist li{position:relative;padding-left:7px}
.checklist li::before{content:"";position:absolute;left:0;top:1.3px;width:4px;height:4px;border-radius:50%;background:var(--orange)}
.checklist li::after{content:"";position:absolute;left:1.1px;top:2.3px;width:1.5px;height:.9px;border-left:.6px solid #fff;border-bottom:.6px solid #fff;transform:rotate(-45deg)}
.body{font-size:5.4px;line-height:1.3;margin-top:4px}
.body + .body{margin-top:7px}
.products{border:1.2px solid var(--rule);margin-top:11px;font-size:5.4px;font-weight:700;color:#111}
.products div{padding:1.5px 4px;border-top:1.2px solid var(--rule);line-height:1.2}
.products .head{border-top:none;color:var(--navy);font-size:6.3px}
.footer-rule{position:absolute;top:694px;height:2px;background:var(--orange)}
.wordmark{position:absolute;top:683px;display:flex;align-items:center;gap:5px;font-weight:600;font-size:16px;color:var(--orange);letter-spacing:.2px}
.wordmark .dot{width:20px;height:20px;border-radius:50%;background:var(--navy)}
.office-table{position:absolute;left:280px;top:276px;width:211px;border-collapse:collapse;font-size:2.6px;line-height:1.1;color:#333;background:#fff;box-shadow:0 0 2px rgba(0,0,0,.25)}
.office-table th,.office-table td{border:.4px solid #9aa6b4;padding:1.1px 1px;height:8px;text-align:left;font-weight:400}
.office-table thead th{background:var(--table-head);font-weight:700;height:5px}
.office-table .grp{background:var(--table-pink);font-weight:700}
.office-table td.f{width:5px;text-align:center}
.office-table tfoot td{background:var(--table-head);font-weight:700;height:5px}
.office-table .blank td{height:5px;background:#fff}
.about-title{position:absolute;left:20px;top:464px;font-size:11px;font-weight:700;color:var(--ink)}
.about-title .accent{color:var(--orange)}
.about-copy{position:absolute;left:20px;top:481px;width:460px;font-size:5.4px;line-height:1.3}
.about-copy p{margin-bottom:6px}
.values{position:absolute;left:21px;top:568px;width:462px;height:98px;background:var(--navy);display:grid;grid-template-columns:repeat(3,1fr);padding:0 14px;column-gap:18px}
.value{position:relative;text-align:center;color:#fff;padding-top:29px}
.value .tile{position:absolute;left:50%;top:-25px;transform:translateX(-50%);width:43px;height:43px;background:var(--orange);border:2.5px solid #fff;box-shadow:0 1px 3px rgba(0,0,0,.3);display:flex;align-items:center;justify-content:center}
.value h3{font-size:6.3px;font-weight:700;margin-bottom:2px}
.value p{font-size:5.4px;line-height:1.25}
</style>
</head>
<body>

<!-- Services page -->
<section class="page page--services">

  <div class="col" style="left:24px;top:27px;width:222px">
    <div class="brand-title"><span class="accent">OUR</span> SERVICES</div>
    <div class="subtitle">Scope of Work Manual</div>
    <h2 class="section-title" style="margin-top:1px">Food Service Equipment Cleaning</h2>
    <div class="shot" style="width:198px;height:89px">
      <div class="frame" style="height:89px"><div class="fill" role="img" aria-label="Soft serve dessert machine in a commercial kitchen" style="background:linear-gradient(100deg,#3b3530,#8a7d6f 45%,#cfc8bd 62%,#4a4440)"></div></div>
    </div>
    <p class="intro">Full Brush Cleaning Service for Marlow, Frostline Slushy, Velaro, Cremora parfait, soft serve and yogurt machines.</p>
    <div class="label">Scope of works – Checklist</div>
    <ul class="checklist">
      <li>Empty Mix</li><li>Reassemble Machine, rinse to clear chemical residue</li>
      <li>Dismantle Machine</li><li>Lube seals and Orings</li>
      <li>Check Orings, shaft, blade and general machine parts</li><li>Fill with Mix and prepare for production</li>
      <li>Clean and sanitise machine thoroughly</li><li></li>
    </ul>
    <div class="label" style="margin-top:8px">Benefits</div>
    <p class="body">Consistent, high quality equipment cleaning supports maintenance of machine to required health and safety standards, extended life of machine and optimal product yield. Utilizing Brightwell allows you to focus staff on core service activities and eliminate the need to continually train new crew members.</p>
    <div class="products"><div class="head">Product used:</div><div>Hartwell Chlorinated Detergent Sanitizers, Food Grade Approved.</div><div>MSDS Available.</div></div>
  </div>

  <div class="col" style="left:272px;top:26px;width:219px">
    <h2 class="section-title">Playground Cleaning</h2>
    <div class="shot" style="width:196px;height:84px">
      <div class="frame" style="height:84px"><div class="fill" role="img" aria-label="Family having fun on colourful playground equipment" style="background:linear-gradient(110deg,#3a6fb8,#d9c24a 40%,#c04a5a 65%,#6d8cc4)"></div></div>
    </div>
    <p class="intro" style="font-size:6.3px">Full cleaning and sanitisation of playground equipment and play area.</p>
    <div class="label">Scope of works – Checklist</div>
    <ul class="checklist">
      <li>High pressure gurney water clean</li><li>Use of non- toxic child friendly chemical</li>
      <li>Detailed scrub of surfaces to remove all grime and debris</li><li>Thorough high-pressure gurney under play structure area and surrounding area.</li>
      <li>Sanitisation inside and out of play ground</li><li>Upgrade * for Graffiti Removal based on consumption.</li>
      <li>Gurney Flooring under play structure</li><li></li>
    </ul>
    <div class="label">Benefits</div>
    <p class="body">Playgrounds are great fun and used by children, during this time they are exposed to a tough external environment, including significant dust and grime from nearby roads and traffic. We pay careful attention to the top of the structure and in and around all areas of the tube and open slides.</p>
    <p class="body">Regular cleaning and sanitization of playgrounds provides effective maintenance results to ensure cleanliness and hygiene standards. This gives peace of mind to parents and mitigates risks for store and playground owners.</p>
    <div class="products" style="margin-top:9px"><div class="head">Product used:</div><div>Purelux and RoseGuard Sanitiser Non Toxic</div><div>Graffiti Removal Product</div><div>MSDS Available</div></div>
  </div>

  <div class="col" style="left:24px;top:366px;width:222px">
    <h2 class="section-title">Kitchen Detail Cleaning Service</h2>
    <div class="shot" style="width:196px;height:84px">
      <div class="frame" style="height:84px"><div class="fill" role="img" aria-label="Chef cleaning a stainless steel kitchen hood" style="background:linear-gradient(100deg,#d8dbe0,#8f969f 45%,#c9ced4 70%,#5e8f8a)"></div></div>
    </div>
    <p class="intro">Full service clean of all kitchen benches and degrease and hot soapy scrub of floor. Additional cleaning can be customized according to client needs.</p>
    <div class="label">Scope of Works – Checklist</div>
    <ul class="checklist">
      <li>Kitchen full foam and sanitization of all kitchen benches,</li><li>Kitchen hoods degreased</li>
      <li>Underneath appliances</li><li>Kitchen floor degreased and full service hot soapy scrub of kitchen floor</li>
      <li>Seals and fridge doors</li><li>Completed with thorough mop and squeegee.</li>
    </ul>
    <div class="label">Benefits</div>
    <p class="body">Clean and fresh, high level hygienic kitchen. Utilizing Brightwell allows your ability to focus on core service activities and provides full support to Team Members.</p>
    <div class="products"><div class="head">Product used:</div><div>TBC FOAM For Kitchen Benches</div><div>TBC DEGREASER AND DETERGENT FOR FLOOR</div><div>MSDS Available</div></div>
  </div>

  <div class="col" style="left:272px;top:366px;width:219px">
    <h2 class="section-title">High Pressure Water Cleaning</h2>
    <div class="shot" style="width:196px;height:84px">
      <div class="frame" style="height:84px"><div class="fill" role="img" aria-label="High pressure water gurney cleaning an outdoor paved area" style="background:linear-gradient(100deg,#3f4a36,#7b8068 35%,#c3c7c4 55%,#4c4c4e)"></div></div>
    </div>
    <p class="intro">High pressure water gurney cleaning service for hard to clean surfaces and common areas.</p>
    <div class="label">Scope of Works – Checklist</div>
    <ul class="checklist">
      <li>Full Service includes cleaning for;</li><li>Walk Ways</li>
      <li>Front of house restaurant, deli or factory</li><li>Back of house</li>
      <li></li><li>Rubbish areas</li>
    </ul>
    <div class="label" style="margin-top:8px">Benefits</div>
    <p class="body">High pressure water gurney cleaning creates a great clean and polished professional environment, this keeps your customers happy and creates a high level hygienic environment for Customers and Team Members.</p>
    <div class="products" style="margin-top:12px"><div class="head">Product used:</div><div>TBC - Sanitizer for path ways</div><div>TBC - Sanitizer for bin aras</div><div>MSDS Available</div></div>
  </div>

  <div class="footer-rule" style="left:4px;width:325px"></div>
  <div class="wordmark" style="left:335px"><span class="dot"></span>Brightwell</div>
</section>

<!-- Detailing, office and about page -->
<section class="page page--more">

  <div class="col" style="left:19px;top:17px;width:230px">
    <h2 class="section-title">Internal Detailing of Parfait Machine Equipment</h2>
    <div class="shot" style="width:196px;height:84px">
      <div class="frame" style="height:84px"><div class="fill" role="img" aria-label="Close-up of built-up residue inside a parfait machine" style="background:linear-gradient(100deg,#2a2a28,#6b6355 45%,#3a3835 70%,#b07a5a)"></div></div>
    </div>
    <p class="intro">Full Degrease and removal of all built up parfait mix that forms over time.</p>
    <div class="label">Scope of works – Checklist</div>
    <ul class="checklist single" style="row-gap:5px">
      <li>Remove sides of machine</li>
      <li>Clean and remove all stale milk build up</li>
      <li>Full Degrease and vacuum area to complete</li>
      <li>Filters are removed and cleaned.</li>
    </ul>
  </div>

  <div class="col" style="left:277px;top:34px;width:206px">
    <div class="shot" style="width:196px;height:84px;margin-top:0">
      <div class="frame" style="height:84px"><div class="fill" role="img" aria-label="Interior machine components of a parfait machine" style="background:linear-gradient(100deg,#1f2022,#5b5d60 45%,#9fa2a4 60%,#2b2c2e)"></div></div>
    </div>
    <div class="label" style="margin-top:18px">Benefits</div>
    <p class="body">Very intensive work and allows for full maintenance of your parfait equipment. Allows professional to do the work for you while your Team Members can focus on core customer service activity.</p>
    <div class="products" style="margin-top:7px"><div class="head">Product used:</div><div>TBC - Degreaser</div></div>
  </div>

  <div class="col" style="left:20px;top:216px;width:212px">
    <h2 class="section-title">General Office Cleaning</h2>
    <div class="shot" style="width:196px;height:84px">
      <div class="frame" style="height:84px"><div class="fill" role="img" aria-label="Cleaning team wiping desks in a bright office" style="background:linear-gradient(100deg,#dfe4ea,#9aa7b8 35%,#2f4466 55%,#d8dde3)"></div></div>
    </div>
    <div class="label" style="margin-top:17px">Scope of works – Checklist</div>
    <ul class="checklist single" style="row-gap:5px">
      <li>Customised to customer requirements</li>
      <li>According to standard cleaning checklist.</li>
    </ul>
    <div class="label">Benefits</div>
    <p class="body">Look after the wellbeing of Team Members with high quality cleaning services so the environment is hygienic.</p>
    <div class="products" style="margin-top:6px"><div class="head">Product used:</div><div style="padding:3px 4px">TBC – Spray for desks</div><div style="padding:3px 4px">TBC – Floor Care</div><div style="padding:3px 4px">TBC – Ladies and Gents Rest Rooms.</div></div>
  </div>

  <table class="office-table" aria-label="Office cleaning frequency checklist">
    <thead><tr><th>AREAS</th><th>DESCRIPTION</th><th colspan="5">FREQUENCY</th><th>AREAS</th><th>DESCRIPTION</th><th colspan="5">FREQUENCY</th></tr></thead>
    <tbody>
      <tr class="grp"><td>RESTROOMS</td><td># of Restrooms:</td><td class="f">D</td><td class="f">W</td><td class="f">B</td><td class="f">M</td><td class="f">O</td><td>EXTERIOR</td><td></td><td class="f">D</td><td class="f">W</td><td class="f">B</td><td class="f">M</td><td class="f">O</td></tr>
      <tr><td>Toilets</td><td>Clean - Sanitize</td><td></td><td></td><td></td><td></td><td></td><td>Trash - Ashtrays</td><td>Empty - Clean</td><td></td><td></td><td></td><td></td><td></td></tr>
      <tr><td>Sinks - Mirrors</td><td>Clean - Sanitize</td><td></td><td></td><td></td><td></td><td></td><td>Doors - Windows</td><td>Wipe Down</td><td></td><td></td><td></td><td></td><td></td></tr>
      <tr><td>Floors - Drains</td><td>Sweep - Mop</td><td></td><td></td><td></td><td></td><td></td><td>Parking - Walks</td><td>Pick up - Sweep</td><td></td><td></td><td></td><td></td><td></td></tr>
      <tr><td>Walls - Doors</td><td>Clean - Dust</td><td></td><td></td><td></td><td></td><td></td><td>Other</td><td></td><td></td><td></td><td></td><td></td><td></td></tr>
      <tr><td>Trash</td><td>Empty - Line</td><td></td><td></td><td></td><td></td><td></td><td class="grp">BREAK ROOM</td><td class="grp"></td><td class="f grp">D</td><td class="f grp">W</td><td class="f grp">B</td><td class="f grp">M</td><td class="f grp">O</td></tr>
      <tr><td>Supplies</td><td>Fill - Restock</td><td></td><td></td><td></td><td></td><td></td><td>Floors</td><td>Sweep - Mop</td><td></td><td></td><td></td><td></td><td></td></tr>
      <tr><td>Other</td><td></td><td></td><td></td><td></td><td></td><td></td><td>Tables - Chairs</td><td>Clean</td><td></td><td></td><td></td><td></td><td></td></tr>
      <tr class="grp"><td>MAIN FLOOR</td><td># of Floors:</td><td class="f">D</td><td class="f">W</td><td class="f">B</td><td class="f">M</td><td class="f">O</td><td>Appliances</td><td>Clean</td><td></td><td></td><td></td><td></td><td></td></tr>
      <tr><td>Floors</td><td>Sweep - Vacuum</td><td></td><td></td><td></td><td></td><td></td><td>Windows - Blinds</td><td>Clean - Dust</td><td></td><td></td><td></td><td></td><td></td></tr>
      <tr><td>Walls - Doors</td><td>Clean - Dust</td><td></td><td></td><td></td><td></td><td></td><td>Other</td><td></td><td></td><td></td><td></td><td></td><td></td></tr>
      <tr><td>Counters</td><td>Clean</td><td></td><td></td><td></td><td></td><td></td><td class="grp">MISC</td><td class="grp"></td><td class="f grp">D</td><td class="f grp">W</td><td class="f grp">B</td><td class="f grp">M</td><td class="f grp">O</td></tr>
      <tr><td>Trash</td><td>Empty - Line</td><td></td><td></td><td></td><td></td><td></td><td>Stock Room</td><td>Dust - Mop</td><td></td><td></td><td></td><td></td><td></td></tr>
      <tr><td>Pictures - Lights</td><td>Dust</td><td></td><td></td><td></td><td></td><td></td><td>Shelving</td><td>Dust</td><td></td><td></td><td></td><td></td><td></td></tr>
      <tr><td>Windows - Sills</td><td>Clean - Dust</td><td></td><td></td><td></td><td></td><td></td><td>Mats - Runners</td><td>Vacuum</td><td></td><td></td><td></td><td></td><td></td></tr>
      <tr><td>Phones</td><td>Clean</td><td></td><td></td><td></td><td></td><td></td><td>Carpets</td><td>Shampoo</td><td></td><td></td><td></td><td></td><td></td></tr>
      <tr><td>Other</td><td></td><td></td><td></td><td></td><td></td><td></td><td>Other</td><td></td><td></td><td></td><td></td><td></td><td></td></tr>
    </tbody>
    <tfoot><tr><td colspan="14">COMMENTS / SPECIAL INSTRUCTIONS:</td></tr></tfoot>
    <tbody><tr class="blank"><td colspan="14"></td></tr><tr class="blank"><td colspan="14"></td></tr><tr class="blank"><td colspan="14"></td></tr></tbody>
  </table>

  <h2 class="about-title"><span class="accent">ABOUT</span> US</h2>
  <div class="about-copy">
    <p>We are Brightwell, a leading, Australian owned, cleaning services company.</p>
    <p>When you work with Brightwell it is easy to do business with us.</p>
    <p>Our people are professional, reliable and service oriented. In every interaction you have; on site, receiving help from our service support staff, or rolling-out new cleaning sites, you will see and feel the benefits of using Brightwell. The pride we take in our work and a prevailing focus on employees, customers and partners, delivers a consistent and superior ongoing service.</p>
  </div>

  <div class="values">
    <div class="value">
      <div class="tile"><svg width="24" height="24" viewBox="0 0 24 24" fill="none" stroke="#fff" stroke-width="1.4"><circle cx="12" cy="7" r="3"/><path d="M12 10v6M6 16h12l-2 5H8z"/></svg></div>
      <h3>OUR PURPOSE</h3>
      <p>To support and extend the life of equipment, maximize product yield and achieve high quality hygiene standards for our food and equipment service clients. We deliver this by ensuring every person in our service chain delivers their work focusing on high quality and reliable cleaning standards.</p>
    </div>
    <div class="value">
      <div class="tile"><svg width="26" height="26" viewBox="0 0 24 24" fill="#fff"><path d="M12 1l1.6 8.4L22 12l-8.4 1.6L12 23l-1.6-9.4L2 12l8.4-2.6z"/></svg></div>
      <h3>OUR VISION</h3>
      <p>A sustainable food service and equipment cleaning company that creates value for customers, supports its employees in work and life and gives back to the community – now and for generations to come.</p>
    </div>
    <div class="value">
      <div class="tile"><svg width="26" height="26" viewBox="0 0 24 24" fill="none" stroke="#fff" stroke-width="1.3"><circle cx="12" cy="12" r="9.5"/><path d="M15.5 8.5l-2 5-5 2 2-5z"/></svg></div>
      <h3>OUR STRATEGY</h3>
      <p>To differentiate ourselves through a prevailing focus on customer service, in everything we do and every interaction we have. We treat our people as skilled cleaning professionals who are the foundation of our company’s sustainability.</p>
    </div>
  </div>

  <div class="footer-rule" style="left:14px;width:325px"></div>
  <div class="wordmark" style="left:345px"><span class="dot"></span>Brightwell</div>
</section>

</body>
</html>
```